Modern business card design for professional copywriter

I'd like a business card design that I can use to have my cards printed out by tavrel.com as a squared corners business card (see artwork and design guidelines here: https://help.tavrel.com/hc/en-gb/sections/300481762-TAVREL-Product-Templates)

The design should be clean and modern and reflect the colours, tone and branding on my website: https://gretafolvane.com.au

Target Market(s)

Professionals, B2B small business owners

Industry/Entity Type

Business

Contact Information for Business Card

Greta Folvane
m: 0427 954 368
e: greta@gretafolvane.com.au
w: gretafolvane.com.au

Font styles to use
Sans Serif

Requirements
Must have
• Tagline: "Smart copywriting for clever business people"
• Brand colours: fd8000, 009984, 666666 and black
Nice to have

```html
<!DOCTYPE html>
<html lang="en">
<head>
<meta charset="utf-8">
<title>Greta Folvane – Business Card</title>
<link href="https://fonts.googleapis.com/css2?family=Lato:wght@400;700&family=Libre+Baskerville:ital,wght@1,700&display=swap" rel="stylesheet">
<style>
  :root {
    --brand-orange: #fd8000;
    --brand-teal: #009984;
    --brand-grey: #666666;
    --brand-black: #000000;
    --card-white: #ffffff;
    --stage: #333333;
  }
  * { box-sizing: border-box; margin: 0; padding: 0; }
  html, body {
    width: 1200px; height: 900px; overflow: hidden;
    background: var(--stage);
    font-family: "Lato", Arial, sans-serif;
  }
  .stage {
    width: 1200px; height: 900px;
    display: flex; flex-direction: column;
    align-items: center; justify-content: center; gap: 40px;
  }
  .card {
    width: 620px; height: 380px;
    position: relative;
  }
  .card--back {
    background: var(--brand-teal);
    color: var(--card-white);
    display: flex; flex-direction: column;
    align-items: center; justify-content: center;
  }
  .wordmark {
    font-family: "Lato", Arial, sans-serif;
    font-weight: 700;
    font-size: 50px;
    line-height: 1;
    letter-spacing: 0.5px;
  }
  .descriptor {
    font-size: 15px;
    letter-spacing: 9px;
    margin-top: 8px;
    margin-left: 150px;
  }
  .card--back .descriptor { color: var(--card-white); }
  .tagline {
    font-family: "Libre Baskerville", Georgia, serif;
    font-style: italic; font-weight: 700;
    font-size: 16px;
    margin-top: 40px;
  }
  .card--front {
    background: var(--card-white);
  }
  .front-brand {
    position: absolute; left: 250px; top: 110px;
  }
  .card--front .wordmark { color: var(--brand-teal); font-size: 46px; }
  .card--front .descriptor { color: var(--brand-grey); margin-left: 120px; }
  .contact-list {
    position: absolute; left: 250px; top: 215px;
    list-style: none;
  }
  .contact-item {
    display: flex; align-items: center; gap: 14px;
    font-size: 21px; font-weight: 700;
    color: var(--brand-grey);
    height: 36px;
  }
  .contact-icon { width: 20px; height: 20px; flex: none; }
</style>
</head>
<body>
<main class="stage">
  <section class="card card--back" aria-label="Card back">
    <div class="wordmark">Greta Folvane</div>
    <div class="descriptor">COPYWRITER</div>
    <p class="tagline">Smart copywriting for clever business people</p>
  </section>

  <section class="card card--front" aria-label="Card front">
    <div class="front-brand">
      <div class="wordmark">Greta Folvane</div>
      <div class="descriptor">COPYWRITER</div>
    </div>
    <ul class="contact-list">
      <li class="contact-item">
        <svg class="contact-icon" viewBox="0 0 20 20" aria-hidden="true">
          <rect x="5" y="1" width="10" height="18" rx="2" fill="var(--brand-orange)"/>
          <rect x="7" y="4" width="6" height="7" fill="#fff"/>
          <circle cx="10" cy="15" r="1.5" fill="#fff"/>
        </svg>
        <span>0427 954 368</span>
      </li>
      <li class="contact-item">
        <svg class="contact-icon" viewBox="0 0 20 20" aria-hidden="true">
          <rect x="1" y="4" width="18" height="12" fill="var(--brand-orange)"/>
          <path d="M1 4 L10 11 L19 4" fill="none" stroke="#fff" stroke-width="1.5"/>
        </svg>
        <span>greta@gretafolvane.com.au</span>
      </li>
      <li class="contact-item">
        <svg class="contact-icon" viewBox="0 0 20 20" aria-hidden="true">
          <circle cx="10" cy="10" r="9" fill="var(--brand-orange)"/>
          <ellipse cx="10" cy="10" rx="4" ry="9" fill="none" stroke="#fff" stroke-width="1.2"/>
          <line x1="1" y1="10" x2="19" y2="10" stroke="#fff" stroke-width="1.2"/>
        </svg>
        <span>gretafolvane.com.au</span>
      </li>
    </ul>
  </section>
</main>
</body>
</html>
```